Vemtra Group: Business Card for a high end technology company

We need a cool new design for our business cards using our cloud logo. We are a technology consulting business. We pride ourselves on be the best of the best. We mainly focus on cloud solutions and managed services. We need a business card that sets us apart from the other technology companies in the area and allows us to stand out.

Target Market(s)

Technology departments, CIO, CEOs, and Information Technology Staff.

Industry/Entity Type

Information Technology

Contact Information for Business Card

Must have the logo and our name.
Must have employee name, email address, office phone, cell phone and website.
Need to have all info on one side a cool design on backside.

Font styles to use
Serif
Sans Serif

Requirements
Must have
• Must have the logo and our name.
• Must have employee name, email address, office phone, cell phone and website.
• Need to have all info on one side a cool design on back side.
• Must be a crisp clean design, not too busy or confusing.

```html
<!DOCTYPE html>
<html lang="en">
<head>
<meta charset="utf-8">
<title>Vemtra Group – Business Card</title>
<link rel="stylesheet" href="https://fonts.googleapis.com/css2?family=Roboto:wght@700&family=Source+Sans+3:wght@400;600&display=swap">
<style>
  :root {
    --page-bg: #e9e7e4;
    --brand-blue: #1e8ff2;
    --brand-blue-deep: #1479d4;
    --accent-line: #5bb8ff;
    --strip-grey: #d9d9d9;
    --card-dark: #363435;
    --tab-white: #ffffff;
    --text-light: #f2f2f2;
    --text-dark: #2b2b2b;
  }
  * { margin: 0; padding: 0; box-sizing: border-box; }
  html, body { width: 1000px; height: 1200px; overflow: hidden; }
  body {
    background: var(--page-bg);
    position: relative;
    font-family: "Source Sans 3", Arial, sans-serif;
  }
  .card {
    position: absolute;
    left: 204px;
    width: 600px;
    height: 412px;
    box-shadow: 0 22px 26px -12px rgba(0,0,0,0.45);
  }
  .card--front { top: 128px; }
  .card--back { top: 631px; }
  .card-shapes { position: absolute; inset: 0; display: block; }
  .card-shapes .band { fill: var(--brand-blue); }
  .card-shapes .band-edge { fill: var(--brand-blue-deep); }
  .card-shapes .strip { fill: var(--strip-grey); }
  .card-shapes .body { fill: var(--card-dark); }
  .card-shapes .tab, .card-shapes .fold { fill: var(--tab-white); }

  .employee-name {
    position: absolute;
    left: 162px; width: 268px; top: 40px;
    text-align: center;
    font-family: "Roboto", Arial, sans-serif;
    font-weight: 700;
    font-size: 31px;
    color: var(--brand-blue);
  }
  .contact {
    position: absolute;
    left: 184px; width: 224px; top: 178px;
    text-align: center;
    color: var(--text-light);
    font-size: 18px;
    line-height: 23px;
  }
  .contact-group { padding: 0; }
  .contact-rule {
    height: 2px;
    background: var(--accent-line);
    margin: 10px 0 14px;
  }
  .brand-lockup {
    position: absolute;
    left: 164px; width: 270px; top: 40px;
    text-align: center;
  }
  .brand-dot {
    display: block;
    width: 70px; height: 70px;
    margin: 0 auto 18px;
    border-radius: 50%;
    background: var(--brand-blue);
  }
  .brand-name {
    font-size: 36px;
    font-weight: 400;
    color: var(--text-dark);
    line-height: 40px;
  }
  .brand-web {
    margin-top: 4px;
    font-size: 11px;
    font-weight: 600;
    color: var(--text-dark);
  }
</style>
</head>
<body>

<section class="card card--front" aria-label="Card front">
  <svg class="card-shapes" width="600" height="412" viewBox="0 0 600 412" aria-hidden="true">
    <rect class="body" x="0" y="0" width="600" height="412"/>
    <rect class="band" x="0" y="0" width="600" height="64"/>
    <rect class="band-edge" x="0" y="64" width="600" height="6"/>
    <rect class="strip" x="0" y="70" width="600" height="8"/>
    <polygon class="fold" points="118,78 162,78 162,120"/>
    <polygon class="fold" points="430,78 474,78 430,120"/>
    <rect class="tab" x="162" y="0" width="268" height="120"/>
  </svg>
  <h1 class="employee-name">Your Name</h1>
  <div class="contact">
    <p class="contact-group">470.555.0182</p>
    <div class="contact-rule"></div>
    <p class="contact-group">2250 Larkmont Ave Suite 410<br>Halden, GA 30416</p>
    <div class="contact-rule"></div>
    <p class="contact-group">info@vemtragroup.com<br>www.vemtragroup.com</p>
  </div>
</section>

<section class="card card--back" aria-label="Card back">
  <svg class="card-shapes" width="600" height="412" viewBox="0 0 600 412" aria-hidden="true">
    <rect class="body" x="0" y="0" width="600" height="412"/>
    <rect class="band" x="0" y="0" width="600" height="188"/>
    <rect class="band-edge" x="0" y="188" width="600" height="5"/>
    <rect class="strip" x="0" y="193" width="600" height="8"/>
    <polygon class="fold" points="120,201 164,201 164,245"/>
    <polygon class="fold" points="434,201 478,201 434,245"/>
    <rect class="tab" x="164" y="0" width="270" height="245"/>
  </svg>
  <div class="brand-lockup">
    <span class="brand-dot"></span>
    <p class="brand-name">Vemtra Group</p>
    <p class="brand-web">www.vemtragroup.com</p>
  </div>
</section>

</body>
</html>
```